We need a banner for this page on our website:
http://www.loganwhitfieldinsight.com/pathways-in-australian-erp/

Dimensions of the image should be approximately 1200 × 500

We are a research-based consultancy and this is a banner to subscribe to our paid content (about corporate technology systems).

Would like the final design to incorporate logo (attached files).
Updates

Banner must include the title "Pathways in Australian ERP"

thanks

Target Market(s)

Business professionals within medium to large Australian organisations and technology companies.

Requirements
Nice to have
• a call to action. something like "subscribe now" or similar. Happy to be directed based on designers customer experience perspective.

Could potentially include "Lifetime Membership"

If including a person consider a male and a female - not one or the other.

```html
<!DOCTYPE html>
<html lang="en">
<head>
<meta charset="utf-8">
<title>Pathways in Australian ERP – Logan Whitfield Insight</title>
<link rel="stylesheet" href="https://fonts.googleapis.com/css2?family=Open+Sans:wght@400;600;700&family=Ubuntu:wght@500;700&display=swap">
<style>
:root{
  --page-bg:#ffffff;
  --header-bg:#ececec;
  --brand-blue:#1e4e9a;
  --nav-link:#2a6aa8;
  --nav-active:#1467b3;
  --tab-bg:#dcdcdc;
  --text-body:#3a3a3a;
  --panel-bg:#f6f6f6;
  --panel-border:#dedede;
  --cta-blue-top:#1a6cc4;
  --cta-blue-bot:#0b4c98;
  --cta-green-top:#b2cc2a;
  --cta-green-bot:#83ab1a;
  --footer-bg:#353535;
  --footer-text:#a8a8a8;
  --footer-head:#ffffff;
  --footer-accent:#f3a228;
}
*{box-sizing:border-box;margin:0;padding:0}
html,body{width:1152px;height:1200px;overflow:hidden;background:var(--page-bg);font-family:"Open Sans",Arial,sans-serif;color:var(--text-body)}
.site-header{position:absolute;left:0;top:0;width:1152px;height:134px;background:var(--header-bg);border-bottom:1px solid #9a9a9a}
.brand{position:absolute;left:30px;top:22px;display:flex;align-items:center;gap:10px}
.brand-mark{width:22px;height:22px;background:var(--brand-blue)}
.brand-name{font-size:19px;font-weight:600;color:var(--brand-blue);letter-spacing:.3px}
.top-nav{position:absolute;right:12px;top:6px;display:flex;font-size:15px}
.top-nav a{color:var(--nav-link);text-decoration:none;padding:5px 12px;line-height:19px}
.top-nav a.active{background:var(--nav-active);color:#fff}
.search{position:absolute;left:322px;top:48px;width:489px;height:30px;background:#fff;border:1px solid #ccc;font-size:14px;color:#444;padding:5px 6px}
.tabs{position:absolute;left:334px;top:100px;display:flex;gap:5px}
.tabs span{background:var(--tab-bg);font-family:"Ubuntu",sans-serif;font-weight:700;font-size:13.5px;color:#111;height:34px;line-height:36px;padding:0 24px}
.hero{position:absolute;left:0;top:134px;width:1152px;height:478px;overflow:hidden}
.hero-photo{position:absolute;inset:0;background:linear-gradient(90deg,#e7e2dc 0%,#f4f4f4 30%,#fafafa 55%,#e6e4e2 75%,#6d6560 100%)}
.hero-title{position:absolute;left:0;width:1152px;top:96px;text-align:center;font-size:48px;font-weight:400;color:#3a3a3a}
.hero-sub{position:absolute;left:0;width:1152px;top:162px;text-align:center;font-size:21px;color:#3a3a3a}
.cta-wrap{position:absolute;left:420px;top:226px;width:312px;height:172px;background:rgba(255,255,255,.55);border-radius:12px}
.cta{position:absolute;left:8px;width:296px;height:71px;border-radius:5px;color:#fff;font-size:21px;font-weight:700;text-align:center;line-height:71px;letter-spacing:.3px}
.cta-subscribe{top:2px;background:linear-gradient(var(--cta-blue-top),var(--cta-blue-bot))}
.cta-register{top:84px;background:linear-gradient(var(--cta-green-top),var(--cta-green-bot))}
.cta-note{position:absolute;left:0;width:1152px;top:394px;text-align:center;font-size:16px;color:#444}
.cta-note b{font-weight:700;color:#333}
.intro{position:absolute;left:168px;top:641px;width:771px;height:393px;background:var(--panel-bg);border:1px solid var(--panel-border);padding:39px 38px 0 39px;font-size:15.4px;line-height:20px}
.intro ul{margin:23px 0 0 42px}
.site-footer{position:absolute;left:0;top:1070px;width:1152px;height:130px;background:var(--footer-bg);font-size:10.5px;color:var(--footer-text)}
.foot-col{position:absolute;top:33px;width:150px}
.foot-col h3{font-size:12.5px;font-weight:700;color:var(--footer-head);margin-bottom:5px}
.foot-col li{list-style:none;padding-left:10px;position:relative;line-height:13.5px;margin-bottom:4px}
.foot-col li::before{content:"";position:absolute;left:0;top:5px;width:4px;height:4px;background:#777}
.foot-col .phone{color:var(--footer-accent)}
</style>
</head>
<body>
<header class="site-header">
  <div class="brand"><span class="brand-mark"></span><span class="brand-name">Logan Whitfield Insight</span></div>
  <nav class="top-nav">
    <a>Services</a><a class="active">Pathways in Australian ERP</a><a>About LW</a><a>Company Info</a><a>How to Subscribe</a><a>Log In</a>
  </nav>
  <div class="search">Search...</div>
  <div class="tabs"><span>Home Page</span><span>Strategy</span><span>Management</span><span>Technology</span></div>
</header>

<section class="hero">
  <div class="hero-photo" role="img" aria-label="Office scene: a smiling man and a woman in a business meeting at a laptop, with hands, pen and printed bar charts on the desk"></div>
  <h1 class="hero-title">Pathways in Australian ERP</h1>
  <p class="hero-sub">Includes&nbsp; with solutions from leading provider</p>
  <div class="cta-wrap">
    <div class="cta cta-subscribe">SUBSCRIBE NOW</div>
    <div class="cta cta-register">REGISTER NOW</div>
  </div>
  <p class="cta-note">- for <b>LIFETIME SUBSCRIPTION</b> -</p>
</section>

<section class="intro">
  <p>LWI is an independent advisory firm focused on delivering organisational and technology risk management outcomes for leading organisations. We also specialise in supporting organisations where CivicStack One solutions are a key platform within the current or future architecture. This includes architectural and business integration with solutions from other leading providers including Norvane, Kestrel, Brightforge, Tessaro, Corvel, Ardent, Assetline, Harlow Prentiss, Quandel, and a range of cloud service providers including Kaimori, Rivermark, Datavale, Nexon Tel and more.</p>
  <ul>
    <li>Key vendor solutions across a range of industries;</li>
    <li>Achievable and cost-effective public sector shared services environments;</li>
    <li>Integrated approaches for extensive fleet, property, and linear asset industries;</li>
    <li>World-leading public and private sector solutions for social services;</li>
    <li>Highly configurable approaches towards student management;</li>
    <li>Information based solutions for enterprise content management; or</li>
    <li>Integrated approaches to planning, performance management and corporate reporting initiatives.</li>
  </ul>
</section>

<footer class="site-footer">
  <div class="foot-col" style="left:264px"><h3>Connect with us</h3><ul><li>Phone: <span class="phone">+61 3 5550 1842.</span> 8:00 a.m. to 5:30 p.m. Australia EDT</li><li>Contact Us</li></ul></div>
  <div class="foot-col" style="left:418px"><h3>Company Info</h3><ul><li>Company Information</li></ul></div>
  <div class="foot-col" style="left:571px"><h3>Information for</h3><ul><li>Strategists</li><li>Managers</li><li>Technologists</li></ul></div>
  <div class="foot-col" style="left:725px;width:140px"><h3>Latest Content</h3><ul><li>Information Management: Queensland's attempt at Citizen-centric Government</li><li>You've bought an ERP</li></ul></div>
</footer>
</body>
</html>
```